Flyer Design Project

We are a storm restoration company that has recently begun restoration from water/flood damage from Hurricane Sandy. We provide disaster relief to homeowners and or commercial property owners after a flood. To start we offer cleanup and remediation which is taking out and disposing of all wet items in a home or business and the cutting out of walls, flooring and other items affected by a flood. We then provide remediation which includes the drying out of a home or business along with a dehumidifier to take all the moisture out of the air and to put it simply dry out the home. We also uses chemicals to clean and provide mold remediation to prevent to growth of mold. We work directly with a customers insurance company if they have flood insurance and after that we provide the services to rebuild and bring their property back to its condition before the storm.

Im looking for an informational type flier that I could insert into our business folders that we give to customers and also to use as fliers to pass out to potential customers. I want potential customers to look at this and feel comfortable with calling my company and working with us.

Company name Brellwick Building Partners. I attached our company logo.

Target Market(s)

Those affected by flooding from Hurricane Sandy

Industry/Entity Type

Insurance

Requirements
Must have
• Company logo, name and colors on flier
Nice to have
• Color photos that have to do with water restoration or showing flood damamge

```html
<!DOCTYPE html>
<html lang="en">
<head>
<meta charset="utf-8">
<title>Brellwick Building Partners – Flood Restoration Flyer</title>
<link rel="stylesheet" href="https://fonts.googleapis.com/css2?family=Open+Sans:wght@400;700;800&display=swap">
<style>
  :root {
    --bg: #e6e7e8;
    --paper: #ffffff;
    --blue: #3597d3;
    --navy: #1f2e6b;
    --orange: #f04e23;
    --yellow: #f5ea14;
    --grey: #d1d2d4;
    --ink: #2a3470;
  }
  * { margin: 0; padding: 0; box-sizing: border-box; }
  html, body { width: 1169px; height: 1200px; overflow: hidden; background: var(--bg); }
  body { position: relative; font-family: "Open Sans", Arial, sans-serif; }

  .flyer { position: absolute; top: 252px; width: 441px; height: 752px; background: var(--paper); overflow: hidden; }
  .flyer--front { left: 110px; }
  .flyer--back { left: 623px; }
  .flyer__art { position: absolute; inset: 0; width: 100%; height: 100%; display: block; }

  .brand {
    position: absolute; left: 128px; top: 126px;
    display: flex; align-items: center; gap: 10px;
  }
  .brand__dot { width: 26px; height: 26px; border-radius: 50%; background: var(--yellow); flex: none; }
  .brand__name { color: var(--navy); font-weight: 800; font-size: 20px; line-height: 1.05; }

  .headline { position: absolute; left: 0; color: #fff; font-weight: 800; line-height: 1; letter-spacing: -2px; white-space: nowrap; }
  .headline--top { top: 366px; font-size: 46px; }
  .headline--main { top: 420px; font-size: 86px; letter-spacing: -5px; }
  .headline--main .headline__you { font-size: 54px; letter-spacing: -2px; margin-left: 4px; }

  .badge {
    position: absolute; color: var(--navy); font-weight: 700; letter-spacing: -1px;
    display: flex; align-items: center; justify-content: center; border-radius: 50%;
  }
  .badge--front { left: 344px; top: 469px; width: 90px; height: 90px; font-size: 29px; }
  .badge--back { left: 33px; top: 34px; width: 112px; height: 112px; font-size: 37px; }

  .services { position: absolute; left: 20px; top: 360px; width: 410px; list-style: none; }
  .services li {
    position: relative; padding-left: 21px; margin-bottom: 20px;
    color: var(--ink); font-size: 14px; line-height: 20.5px;
  }
  .services li svg { position: absolute; left: 0; top: 3px; width: 15px; height: 15px; }
</style>
</head>
<body>

<section class="flyer flyer--front" aria-label="Flyer front">
  <svg class="flyer__art" viewBox="0 0 494 843" preserveAspectRatio="none" aria-hidden="false">
    <defs>
      <linearGradient id="hall" x1="0" y1="0" x2="0" y2="1">
        <stop offset="0" stop-color="#e9ecea"/><stop offset="0.45" stop-color="#a9b0a4"/><stop offset="1" stop-color="#4d5a44"/>
      </linearGradient>
      <linearGradient id="office" x1="0" y1="0" x2="1" y2="1">
        <stop offset="0" stop-color="#6a6e66"/><stop offset="1" stop-color="#9a9b8c"/>
      </linearGradient>
      <linearGradient id="room" x1="0" y1="0" x2="1" y2="1">
        <stop offset="0" stop-color="#8c8478"/><stop offset="1" stop-color="#5a5248"/>
      </linearGradient>
    </defs>
    <rect class="photo" x="0" y="250" width="494" height="340" fill="url(#hall)" role="img" aria-label="Photo of a flooded school hallway"/>
    <polygon points="0,0 494,0 494,150 280,255 0,430" fill="#fff"/>
    <polygon points="0,0 430,0 0,150" fill="var(--blue)"/>
    <polygon points="0,150 430,0 494,0 494,2 0,192" fill="var(--orange)"/>
    <polygon points="280,255 494,150 494,255" fill="var(--navy)"/>
    <rect x="0" y="566" width="494" height="14" fill="#fff"/>
    <rect x="0" y="583" width="494" height="9" fill="var(--yellow)"/>
    <rect x="0" y="597" width="232" height="173" fill="url(#office)" role="img" aria-label="Photo of water-damaged computers on a desk"/>
    <rect x="237" y="597" width="257" height="173" fill="url(#room)" role="img" aria-label="Photo of a flood-damaged living room"/>
    <rect x="0" y="800" width="494" height="43" fill="var(--orange)"/>
    <circle cx="436" cy="576" r="50" fill="var(--yellow)"/>
  </svg>
  <div class="brand">
    <span class="brand__dot"></span>
    <span class="brand__name">Brellwick<br>Building Partners</span>
  </div>
  <h1 class="headline headline--top">LET US</h1>
  <p class="headline headline--main">HELP<span class="headline__you">YOU</span></p>
  <div class="badge badge--front">24h/7</div>
</section>

<section class="flyer flyer--back" aria-label="Flyer back">
  <svg class="flyer__art" viewBox="0 0 494 843" preserveAspectRatio="none">
    <defs>
      <linearGradient id="house" x1="0" y1="0" x2="0" y2="1">
        <stop offset="0" stop-color="#8f9a6e"/><stop offset="0.5" stop-color="#c9cbc2"/><stop offset="1" stop-color="#5b5a3e"/>
      </linearGradient>
      <linearGradient id="cleanup" x1="0" y1="0" x2="1" y2="1">
        <stop offset="0" stop-color="#3a6b78"/><stop offset="1" stop-color="#6e5744"/>
      </linearGradient>
    </defs>
    <polygon points="0,0 385,0 0,112" fill="var(--blue)"/>
    <polygon points="0,112 385,0 408,0 0,120" fill="#fff"/>
    <polygon points="170,112 480,4 494,4 494,12 190,118" fill="var(--yellow)"/>
    <rect x="0" y="188" width="262" height="175" fill="url(#house)" role="img" aria-label="Photo of a house surrounded by floodwater"/>
    <rect x="266" y="188" width="228" height="175" fill="url(#cleanup)" role="img" aria-label="Photo of a worker clearing a flooded classroom"/>
    <polygon points="0,608 494,405 494,843 0,843" fill="var(--grey)"/>
    <polygon points="228,843 494,760 494,843" fill="var(--orange)"/>
    <circle cx="100" cy="100" r="62" fill="var(--yellow)"/>
  </svg>
  <div class="badge badge--back">24h/7</div>
  <ul class="services">
    <li><svg viewBox="0 0 24 24"><polygon points="12,1 15,9 23,9 16.5,14 19,22 12,17 5,22 7.5,14 1,9 9,9" fill="var(--navy)"/></svg>We offer cleanup and remediation which is taking out and disposing of all wet items in a home or business and the cutting out of walls, flooring and other items affected by a flood.</li>
    <li><svg viewBox="0 0 24 24"><polygon points="12,1 15,9 23,9 16.5,14 19,22 12,17 5,22 7.5,14 1,9 9,9" fill="var(--navy)"/></svg>We then provide remediation which includes the drying out of a home or business along with a dehumidifier to take all the moisture out of the air and to put it simply dry out the home.</li>
    <li><svg viewBox="0 0 24 24"><polygon points="12,1 15,9 23,9 16.5,14 19,22 12,17 5,22 7.5,14 1,9 9,9" fill="var(--navy)"/></svg>We also uses chemicals to clean and provide mold remediation to prevent to growth of mold.</li>
    <li><svg viewBox="0 0 24 24"><polygon points="12,1 15,9 23,9 16.5,14 19,22 12,17 5,22 7.5,14 1,9 9,9" fill="var(--navy)"/></svg>We work directly with a customers insurance company if they have flood insurance and after that we provide the services to rebuild and bring their property back to its condition before the storm.</li>
  </ul>
</section>

</body>
</html>
```